BrXpertz Business Cards for SME Experts

We need a business card for a new company based in Clearwater FL called Kestrel of Merit. KoM is your access to on-demand subject matter experts. The final design should be very clean communicating innovation and expertise. Our logo design is attached.

The Information Age has affected the workforce in that automation and computerization have resulted in higher productivity coupled with net job loss of many knowledgeable employees. Combined with the creation of the internet and search capabilities, the disintermediation of the value chain of Subject Matter Experts (SME) has happened. We no longer need to work through traditional consulting firms for all consulting needs, instead the direct access to the SME, through a leaner and lower cost model is what the market is demanding.
BrXpertz is a new marketplace to buy consulting services. The business model is that all consultants (subject matter experts) can become a consulting resource in the marketplace following our guidelines. The consumer can now easily access consultants that they could not find easily before.
In much the way an Zyla car can be identified and requested, so can a BrXpertz Consultant. Each consultant can be identified by: location, expertise, billing rate, and prior experience rating.
By seamlessly connecting consultants to requesters through a new Kestrel of Merit marketplace, you now will have an easy to use and quicker turnaround to request and staff your consulting needs. Leveraging the KoM app, you can access the subject matter expert you need for your business requirement.

Target Market(s)

Small and medium sized companies; non-profits

Industry/Entity Type

Business Consultant

Contact Information for Business Card

Name
website
email address
Logo
mailing address (debating if I really need...)
twitter
LinkedIn

Requirements
Must have
• the logo I have included in the design; want the colors to be consistent with the logo design

```html
<!DOCTYPE html>
<html lang="en">
<head>
<meta charset="utf-8">
<title>Kestrel of Merit – Business Card</title>
<link href="https://fonts.googleapis.com/css2?family=Mulish:wght@800&family=PT+Sans:wght@400;700&display=swap" rel="stylesheet">
<style>
  :root {
    --backdrop: #3b3532;
    --card: #f4f4f3;
    --navy: #1d2a6b;
    --cyan: #1ca3d6;
    --ink: #1c1c22;
    --shadow: rgba(0,0,0,0.45);
  }
  * { margin: 0; padding: 0; box-sizing: border-box; }
  html, body {
    width: 1200px; height: 844px; overflow: hidden;
    background: var(--backdrop);
  }
  .stage { position: relative; width: 1200px; height: 844px; }
  .card {
    position: absolute;
    width: 520px; height: 300px;
    top: 272px;
    background: var(--card);
    box-shadow: 0 10px 28px var(--shadow);
  }
  .card--front { left: 50px; }
  .card--back { left: 630px; }

  .brand-mark {
    position: absolute;
    width: 62px; height: 62px;
    border: 4px solid var(--navy);
    border-radius: 50%;
  }
  .brand-name {
    position: absolute;
    font-family: "Mulish", sans-serif;
    font-weight: 800;
    color: var(--navy);
    white-space: nowrap;
    letter-spacing: 0.5px;
  }
  .card--front .brand-mark { left: 197px; top: 60px; }
  .card--front .brand-name { left: 138px; top: 136px; font-size: 24px; }
  .card--back .brand-mark { left: 229px; top: 78px; width: 64px; height: 64px; }
  .card--back .brand-name { left: 0; width: 520px; text-align: center; top: 158px; font-size: 27px; }

  .contact-list {
    position: absolute;
    right: 26px; top: 124px;
    list-style: none;
    font-family: "PT Sans", sans-serif;
    font-size: 13px;
    color: var(--ink);
    text-align: right;
    line-height: 22px;
  }
  .contact-list li { display: flex; justify-content: flex-end; align-items: center; gap: 7px; }
  .contact-icon { width: 11px; height: 11px; flex: none; }

  .holder {
    position: absolute; left: 30px; top: 208px;
    font-family: "PT Sans", sans-serif;
  }
  .holder-name { font-size: 21px; font-weight: 700; color: var(--navy); }
  .holder-address { font-size: 13.5px; color: var(--ink); line-height: 16px; margin-top: 4px; }
</style>
</head>
<body>
<main class="stage">
  <section class="card card--front" aria-label="Card front">
    <div class="brand-mark"></div>
    <div class="brand-name">Kestrel of Merit</div>

    <ul class="contact-list">
      <li>info@kestrelmerit.com
        <svg class="contact-icon" viewBox="0 0 12 12"><rect x="1" y="2.5" width="10" height="7" fill="none" stroke="var(--navy)" stroke-width="1.4"/><path d="M1 2.5 L6 6.5 L11 2.5" fill="none" stroke="var(--navy)" stroke-width="1.2"/></svg>
      </li>
      <li>www.kestrelmerit.com
        <svg class="contact-icon" viewBox="0 0 12 12"><path d="M5 7 L7 5" stroke="var(--navy)" stroke-width="1.4"/><rect x="1.5" y="5.5" width="5" height="3" rx="1.5" transform="rotate(-45 4 7)" fill="none" stroke="var(--navy)" stroke-width="1.2"/><rect x="5.5" y="3.5" width="5" height="3" rx="1.5" transform="rotate(-45 8 5)" fill="none" stroke="var(--navy)" stroke-width="1.2"/></svg>
      </li>
      <li>Yourname/chirpline.com
        <svg class="contact-icon" viewBox="0 0 12 12"><circle cx="6" cy="6" r="5" fill="var(--navy)"/></svg>
      </li>
      <li>Yourname/proconnect.com
        <svg class="contact-icon" viewBox="0 0 12 12"><rect x="1" y="1" width="10" height="10" fill="var(--navy)"/></svg>
      </li>
    </ul>

    <div class="holder">
      <div class="holder-name">Daniel Harlow</div>
      <div class="holder-address">12345, Address Goes Here<br>Country Name, 123456</div>
    </div>
  </section>

  <section class="card card--back" aria-label="Card back">
    <div class="brand-mark"></div>
    <div class="brand-name">Kestrel of Merit</div>
  </section>
</main>
</body>
</html>
```